" Assessoria e consultoria de projetos agropecuários com foco em bovinos. DIFERENCIAIS ? Atendimento personalizado; ? Foco em processos; Melhoria continua - metodologia LEAN ? Foco no cliente e na qualidade do serviço; ? Acompanhamento dos resultados gerados pela consultoria; ? Serviço com conhecimento agregado. Atendimento personalizado: A Brota enxerga a necessidade do contato personalizado com o cliente, demonstrando constantemente que a empresa está interessada em ajudá-lo e trazer soluções para seus problemas. ? Foco em processos: Como a maioria das empresas que prestam consultoria na área estão mais voltadas para TÉCNICAS animal, o foco em processos e gestao por processos torna-se um diferencial da Brota. A empresa poderia aproveitar essa vantagem divulgando a importância do gerenciamento eficaz nas fazendas através dos processos agropecuários. ? Foco no cliente e na qualidade do serviço: Através do atendimento personalizado, o consultor da Brota tem a responsabilidade de manter o comprometimento com o cliente e com a qualidade dos serviços entregues. Assim, a empresa cria uma boa relação com os consumidores, fidelizando-os. ? Acompanhamento dos resultados gerados pela consultoria: Além de prestar consultoria, a Empresa auxilia o cliente a implementar as técnicas e soluções, fazendo o acompanhamento de resultados com indicadores. ? Serviço com maior valor agregado: Através da constante busca por conhecimento na área, a qualidade dos projetos entregues será cada vez maior, consequentemente tornando-os mais eficazes e eficientes. "

```html
<!DOCTYPE html>
<html lang="pt-BR">
<head>
<meta charset="utf-8">
<title>Brota – Papelaria</title>
<link rel="stylesheet" href="https://fonts.googleapis.com/css2?family=Montserrat:wght@400;500;600&display=swap">
<style>
  :root {
    --navy-deep: #0b1a33;
    --navy: #16294a;
    --green: #3fae5e;
    --green-light: #7bd38f;
    --paper: #f7f8f9;
    --ink-soft: #c9d1dc;
    --backdrop: #e8eaed;
  }
  * { box-sizing: border-box; margin: 0; padding: 0; }
  html, body {
    width: 1200px; height: 1200px; overflow: hidden;
    background: var(--backdrop);
    font-family: "Montserrat", sans-serif;
  }
  .stationery {
    position: absolute; top: 340px; left: 45px;
    display: flex; gap: 45px;
  }
  .sheet {
    position: relative; width: 340px; height: 480px; overflow: hidden;
    box-shadow: 0 10px 24px rgba(0,0,0,.18);
  }
  .folder {
    background: radial-gradient(ellipse at 50% 40%, var(--navy) 0%, var(--navy-deep) 75%);
  }
  .green-band {
    position: absolute; left: 0; right: 0; bottom: 0; height: 30px;
    background: linear-gradient(180deg, var(--green-light), var(--green));
  }
  .brand-mark {
    display: flex; flex-direction: column; align-items: center; gap: 6px;
    color: #fff; font-weight: 500;
  }
  .brand-mark .dot {
    width: 26px; height: 26px; border-radius: 50%;
    border: 3px solid var(--ink-soft);
  }
  .brand-mark .name { font-size: 13px; letter-spacing: 4px; }
  .folder-back .brand-mark { position: absolute; top: 150px; left: 0; right: 0; }
  .contact {
    position: absolute; left: 40px; bottom: 52px;
    color: var(--ink-soft); font-size: 8px; line-height: 1.6;
  }
  .letterhead { background: var(--paper); }
  .letterhead .brand-mark {
    position: absolute; top: 20px; left: 0; right: 0; color: var(--navy);
  }
  .letterhead .brand-mark .dot { width: 18px; height: 18px; border-width: 2px; border-color: var(--green); }
  .letterhead .brand-mark .name { font-size: 9px; letter-spacing: 3px; }
  .letterhead-footer {
    position: absolute; left: 0; right: 0; bottom: 0; height: 26px;
    background: var(--navy-deep); border-top: 4px solid var(--green);
  }
  .folder-front .brand-mark { position: absolute; top: 145px; left: 0; right: 0; gap: 10px; }
  .folder-front .brand-mark .dot { width: 40px; height: 40px; border-width: 4px; }
  .folder-front .brand-mark .name { font-size: 34px; letter-spacing: 14px; padding-left: 14px; }
  .tagline { font-size: 7px; letter-spacing: 2px; color: var(--ink-soft); font-weight: 400; }
</style>
</head>
<body>
  <main class="stationery">
    <section class="sheet folder folder-back">
      <div class="brand-mark">
        <span class="dot"></span>
        <span class="name">BROTA</span>
      </div>
      <address class="contact">
        +55 11 4000-1234<br>
        R. Campos, 120 - 00000-000<br>
        contato@brota.com.br
      </address>
      <div class="green-band"></div>
    </section>

    <section class="sheet letterhead">
      <div class="brand-mark">
        <span class="dot"></span>
        <span class="name">BROTA</span>
      </div>
      <div class="letterhead-footer"></div>
    </section>

    <section class="sheet folder folder-front">
      <div class="brand-mark">
        <span class="dot"></span>
        <span class="name">BROTA</span>
        <span class="tagline">CONSULTORIA AGROPECUÁRIA</span>
      </div>
      <div class="green-band"></div>
    </section>
  </main>
</body>
</html>
```